Venture Capital Investment Firm

We are looking to overhaul our existing website (substantially), with only using the same logos (which we can provide).
We are an investment firm that focuses on making loans to late stage technology companies. Our site should ultimately look like other venture capital firms, and look modern and fresh. We have an existing website www.northvaleloan.com which this will be replacing, although we will be using a lot of the existing written content, and potentially the numbers of pages we will need, we are not wed to anything else. Please feel free to shoot any questions at any time and thank you in advance for your help!
Websites we like as examples:
https://www.tkbrandel.com/
https://www.emberwoodfunds.com/
Target Market(s)
Potential investors who will invest in our firm, as well as potentially companies that are looking to borrow money from us.

```html
<!DOCTYPE html>
<html lang="en">
<head>
<meta charset="utf-8">
<title>Northvale Loan — Partners for Growth</title>
<link rel="stylesheet" href="https://fonts.googleapis.com/css2?family=Montserrat:wght@400;500;700&display=swap">
<style>
  :root {
    --accent: #ffb955;
    --navy: #35356f;
    --navy-deep: #262558;
    --navy-light: #5a5f9a;
    --ink: #2e2e2e;
    --body: #333333;
    --white: #ffffff;
    --paper: #ffffff;
  }
  * { box-sizing: border-box; margin: 0; padding: 0; }
  html, body { width: 1200px; height: 2802px; overflow: hidden; }
  body {
    position: relative;
    background: var(--paper);
    font-family: "Montserrat", sans-serif;
    color: var(--body);
  }
  .abs { position: absolute; }

  /* Hero */
  .hero {
    left: 0; top: 0; width: 1200px; height: 675px;
    background: linear-gradient(160deg, var(--navy-deep) 0%, var(--navy) 40%, var(--navy-light) 70%, var(--navy) 100%);
  }
  .brand {
    left: 172px; top: 10px; height: 36px;
    display: flex; align-items: center; gap: 10px;
    color: var(--white); font-weight: 500; font-size: 20px; letter-spacing: 0.3px;
  }
  .brand-mark { width: 26px; height: 26px; border-radius: 50%; background: var(--white); }
  .nav-link {
    top: 22px; font-size: 10.5px; font-weight: 700; color: var(--white);
    line-height: 12px; white-space: nowrap;
  }
  .register-btn {
    left: 928px; top: 16px; width: 100px; height: 25px;
    background: var(--white); color: var(--ink); border-radius: 2px;
    font-size: 10px; font-weight: 700; display: flex; align-items: center; justify-content: center;
  }
  .hero-title {
    left: 172px; top: 246px; font-size: 33px; font-weight: 700; color: var(--accent);
    letter-spacing: 0.2px; white-space: nowrap;
  }
  .hero-lead {
    left: 172px; top: 309px; width: 430px; font-size: 15.5px; line-height: 23px; color: var(--white);
  }
  .hero-wordmark {
    left: 742px; top: 300px; display: flex; align-items: center; gap: 16px;
    color: var(--white); font-size: 46px; font-weight: 500; white-space: nowrap;
  }
  .hero-wordmark .dot { width: 56px; height: 56px; border-radius: 50%; background: var(--white); }

  .btn {
    width: 212px; height: 37px; background: var(--accent); color: var(--white);
    font-size: 16px; font-weight: 700; display: flex; align-items: center; justify-content: center;
    letter-spacing: 0.3px;
  }

  .section-title { font-size: 34px; font-weight: 700; color: var(--accent); letter-spacing: 0.3px; white-space: nowrap; }
  .copy { font-size: 15px; line-height: 22.6px; color: var(--body); }

  /* Who are we */
  .who-photo {
    left: 0; top: 762px; width: 534px; height: 502px;
    border-radius: 0 251px 251px 0 / 0 251px 251px 0;
    background: linear-gradient(135deg, #9fc0bd 0%, #d7e3df 45%, #6d8f90 100%);
  }
  .divider {
    left: 0; width: 1200px; height: 6px;
    background: linear-gradient(to bottom, rgba(0,0,0,0.06), rgba(0,0,0,0));
  }

  /* Strategy */
  .strategy-photo {
    left: 749px; top: 1443px; width: 451px; height: 491px;
    clip-path: polygon(47% 0, 100% 0, 100% 100%, 46% 100%, 0 79%, 0 25%);
    background: radial-gradient(circle at 60% 40%, #d8d8d8 0%, #6e6e6e 40%, #161616 100%);
  }

  /* Team */
  .team-title { left: 0; width: 1200px; top: 2116px; text-align: center; }
  .team-photo {
    top: 2347px; width: 285px; height: 253px;
    background: radial-gradient(ellipse at 50% 60%, #5a5a5a 0%, #1c1c1c 55%, #0c0c0c 100%);
  }
  .team-name {
    top: 2619px; width: 285px; text-align: center;
    font-size: 16px; font-weight: 700; color: var(--ink); letter-spacing: 0.3px;
  }
</style>
</head>
<body>
  <header class="abs hero">
    <div class="abs brand"><span class="brand-mark"></span>Northvale Loan</div>
    <nav>
      <span class="abs nav-link" style="left:541px;">HOME</span>
      <span class="abs nav-link" style="left:598px;">STRATEGY</span>
      <span class="abs nav-link" style="left:677px;">ABOUT</span>
      <span class="abs nav-link" style="left:740px;">TEAM</span>
      <span class="abs nav-link" style="left:795px;">NEWS</span>
      <span class="abs nav-link" style="left:852px;">CONTACT</span>
    </nav>
    <div class="abs register-btn">REGISTER</div>
    <h1 class="abs hero-title">PARTNERS FOR GROWTH</h1>
    <p class="abs hero-lead">We are a global structured credit investment firm focused on the healthcare and technology industries</p>
    <div class="abs btn" style="left:172px;top:378px;">LEARN MORE</div>
    <div class="abs hero-wordmark"><span class="dot"></span>Northvale</div>
  </header>

  <section>
    <div class="abs who-photo" role="img" aria-label="Two people reviewing notes at a desk between laptops"></div>
    <h2 class="abs section-title" style="left:573px;top:858px;">WHO ARE WE</h2>
    <p class="abs copy" style="left:573px;top:922px;width:465px;">Northvale Loan is a private investment firm unique in its dual focus on life science and technology credit opportunities. Our ambidextrous approach to investing reflects a broad recognition and appreciation for the critical role intellectual property plays in the successful commercialization of products.&nbsp; We apply our extensive industry expertise to assess the revenue visibility created by these assets and offer a range of creative financing solutions.</p>
    <div class="abs btn" style="left:573px;top:1129px;">LEARN MORE</div>
  </section>

  <div class="abs divider" style="top:1351px;"></div>

  <section>
    <h2 class="abs section-title" style="left:172px;top:1533px;">OUR STRATEGY</h2>
    <p class="abs copy" style="left:172px;top:1597px;width:430px;">Our focus spans the life science and technology industries, two sectors where intellectual property (IP) is an integral driver of asset and enterprise value.</p>
    <p class="abs copy" style="left:172px;top:1687px;width:430px;">Our broad experience in investing, technology evaluation, and product forecasting affords us a unique understanding of the value of assets in these dynamic sectors, allowing us to see value where others cannot.</p>
    <div class="abs btn" style="left:172px;top:1807px;">LEARN MORE</div>
    <div class="abs strategy-photo" role="img" aria-label="Black and white chess pieces on a board"></div>
  </section>

  <div class="abs divider" style="top:2026px;"></div>

  <section>
    <h2 class="abs section-title team-title">MEET THE TEAM</h2>
    <p class="abs copy" style="left:172px;top:2181px;width:866px;">We bring over 40 years of collective experience to our investments, including over $1.2B invested within structured credit, milestones and royalties, and the acquisition of legacy assets from some of the world's largest and most well respected pharmaceutical companies.&nbsp; In addition, members of the Northvale Loan team have played senior roles in executing over $75B of M&amp;A, equity, and debt financings in the life science and technology sectors.</p>
    <div class="abs team-photo" style="left:172px;" role="img" aria-label="Portrait of Elias Morrow"></div>
    <div class="abs team-photo" style="left:458px;" role="img" aria-label="Portrait of Samir Calloway"></div>
    <div class="abs team-photo" style="left:743px;" role="img" aria-label="Portrait of Owen Hartley"></div>
    <div class="abs team-name" style="left:172px;">ELIAS MORROW</div>
    <div class="abs team-name" style="left:458px;">SAMIR CALLOWAY</div>
    <div class="abs team-name" style="left:743px;">OWEN HARTLEY</div>
    <div class="abs btn" style="left:494px;top:2671px;">LEARN MORE</div>
  </section>

  <div class="abs divider" style="top:2796px;"></div>
</body>
</html>
```